Mezzanine Floor Manufacturer looking for a new business card design

We manufacture mezzanine floors and are providers of racking systems. We provide a range of items/services - simple rack repairs , full warehouse fit outs , manufacturer and install mezzanine floors , partitioning and large turnkey projects. Recently had a new website - www.corrowden-racking.co.uk and would like our business cards updating aswell . Our current card is single sided in the old logo colours (pdf attached) and needs updating.

Target Market(s)

We deal with large projects/ multi national companies and also smaller projects and companies throughout the UK ranging from a single warehouse to a large multi site company.

Industry/Entity Type

Business

Contact Information for Business Card

Will have job title,tel no's, email ,website address etc like example pdf

Requirements
Must have
• Hi - needs to use the colours of the logo & new website. Card needs to be professional

```html
<!DOCTYPE html>
<html lang="en">
<head>
<meta charset="utf-8">
<title>Corrowden Racking Ltd – Business Card</title>
<link href="https://fonts.googleapis.com/css2?family=Open+Sans:wght@400;700&display=swap" rel="stylesheet">
<style>
  :root {
    --page: #f2ede4;
    --red-deep: #bf1e2b;
    --red-mid: #d11c2e;
    --red-bright: #e21f36;
    --white: #ffffff;
    --ink: #222222;
  }
  * { margin: 0; padding: 0; box-sizing: border-box; }
  html, body {
    width: 1189px; height: 1200px; overflow: hidden;
    background: var(--page);
    font-family: "Open Sans", Arial, sans-serif;
  }
  .card {
    position: absolute; left: 171px; width: 856px; height: 488px;
    overflow: hidden;
    box-shadow: 4px 6px 10px rgba(0,0,0,0.25);
  }
  .red-surface {
    background: linear-gradient(115deg,
      var(--red-bright) 0%, var(--red-deep) 22%, var(--red-mid) 40%,
      var(--red-bright) 55%, var(--red-deep) 72%, var(--red-bright) 100%);
  }
  .card--front { top: 67px; background: var(--white); }
  .card--back { top: 627px; }

  .front-header {
    height: 168px; text-align: center; color: var(--white);
    padding-top: 42px;
  }
  .company-name { font-weight: 700; font-size: 48px; line-height: 1; letter-spacing: 0.3px; }
  .front-email { font-size: 24px; margin-top: 14px; }

  .front-body { position: relative; height: 257px; }
  .brand-mark {
    position: absolute; left: 58px; top: 50px; width: 298px; height: 147px;
    display: flex; align-items: center; justify-content: center;
    color: var(--red-mid); font-weight: 700; font-size: 42px; letter-spacing: 1px;
  }
  .contact { position: absolute; left: 419px; top: 22px; }
  .contact-name { color: var(--red-mid); font-weight: 700; font-size: 30px; line-height: 1; }
  .contact-role { color: var(--ink); font-size: 22px; line-height: 1.1; }
  .phone-list { list-style: none; margin-top: 44px; }
  .phone-list li {
    display: flex; align-items: center; gap: 8px;
    font-size: 24px; color: var(--ink); line-height: 32px;
  }
  .phone-list svg { width: 22px; height: 22px; flex: none; }

  .front-footer {
    height: 63px; color: var(--white); font-size: 22px;
    display: flex; align-items: center; justify-content: center;
  }

  .back-title {
    position: absolute; left: 56px; top: 70px; color: var(--white);
  }
  .services { position: absolute; left: 59px; top: 195px; color: var(--white); }
  .services-heading { font-weight: 700; font-size: 28px; letter-spacing: 0.5px; margin-bottom: 22px; }
  .services-list { list-style: none; }
  .services-list li { font-size: 23px; line-height: 28.5px; display: flex; align-items: center; }
  .services-list li::before {
    content: ""; width: 14px; height: 14px; border-radius: 50%;
    background: var(--white); margin-right: 19px;
  }
  .back-web {
    position: absolute; left: 59px; top: 410px; color: var(--white); font-size: 23px;
  }
  .social-links { position: absolute; left: 555px; top: 400px; display: flex; gap: 23px; }
  .social-links span { width: 44px; height: 44px; background: var(--white); display: block; }
</style>
</head>
<body>

<section class="card card--front">
  <header class="front-header red-surface">
    <h1 class="company-name">Corrowden Racking Ltd</h1>
    <p class="front-email">sales@corrowden-racking.co.uk</p>
  </header>
  <div class="front-body">
    <div class="brand-mark">CORROWDEN</div>
    <div class="contact">
      <p class="contact-name">DANIEL HARTLEY</p>
      <p class="contact-role">TECHNICAL SALES</p>
      <ul class="phone-list">
        <li>
          <svg viewBox="0 0 22 22" aria-label="mobile"><rect width="22" height="22" fill="#d11c2e"/><rect x="7" y="3" width="8" height="16" rx="1.5" fill="#fff"/><rect x="8.5" y="5" width="5" height="5" fill="#d11c2e"/></svg>
          07700 900412
        </li>
        <li>
          <svg viewBox="0 0 22 22" aria-label="telephone"><rect width="22" height="22" fill="#d11c2e"/><path d="M4 9c0-3 14-3 14 0v2h-4V9.5H8V11H4z" fill="#fff"/><rect x="6" y="12" width="10" height="6" rx="1" fill="#fff"/></svg>
          01632 960581
        </li>
        <li>
          <svg viewBox="0 0 22 22" aria-label="fax"><rect width="22" height="22" fill="#d11c2e"/><rect x="6" y="3" width="10" height="6" fill="#fff"/><rect x="3" y="10" width="16" height="8" rx="1" fill="#fff"/><rect x="6" y="13" width="10" height="2" fill="#d11c2e"/></svg>
          01632 960927
        </li>
      </ul>
    </div>
  </div>
  <footer class="front-footer red-surface">
    Kestrel Way Milford Trade Park Belper Derbyshire DE9 4LT
  </footer>
</section>

<section class="card card--back red-surface">
  <h2 class="company-name back-title">Corrowden Racking Ltd</h2>
  <div class="services">
    <h3 class="services-heading">SERVICES</h3>
    <ul class="services-list">
      <li>simple rack repairs</li>
      <li>full warehouse fit outs</li>
      <li>manufacturer and install mezzanine floors</li>
      <li>partitioning and large turnkey projects</li>
    </ul>
  </div>
  <p class="back-web">www.corrowden-racking.co.uk</p>
  <div class="social-links" aria-label="social media links">
    <span></span><span></span><span></span><span></span>
  </div>
</section>

</body>
</html>
```